Bramblet Ecommerce Website Design - Tarvex & Brenvik Growth *

The goal of this website is to show case studies and testimonials for Bramblet Ecommerce. Our company specializes in Tarvex and Brenvik management and growth. The design should communicate trust, growth, and attention to detail.

Below are 3 leading websites in the space
https://varelmoxgroup.com/solutions
https://pellorstudio.com/
https://qobrena.com/

Target Market(s)

Businesses looking to grow on Tarvex. Small and large businesses are our clients. Many are brands that are household names.

Industry/Entity Type

Ecommerce

Number of Pages Required

5+ page

Font styles to use
Serif
Sans Serif

```html
<!DOCTYPE html>
<html lang="en">
<head>
<meta charset="utf-8">
<title>Bramblet Ecommerce</title>
<link rel="stylesheet" href="https://fonts.googleapis.com/css2?family=Old+Standard+TT:ital,wght@0,400;0,700;1,400&family=Montserrat:ital,wght@0,400;0,500;0,700;1,400&family=Poppins:wght@700;800&display=swap">
<style>
:root{
  --green:#0bb03a;
  --green-dark:#0a7a2a;
  --forest:#032a14;
  --ink:#1d1d1d;
  --body:#444;
  --muted:#777;
  --hero-bg:#f4f4f4;
  --blush:#fdeff0;
  --lavender:#f1f0f8;
  --cream:#fdfbec;
  --sky:#f2f5fb;
  --white:#fff;
}
*{margin:0;padding:0;box-sizing:border-box}
html,body{width:1200px;height:3048px;overflow:hidden;background:var(--white)}
body{font-family:"Montserrat",sans-serif;color:var(--body)}
.page{position:relative;width:1200px;height:3048px;overflow:hidden;background:var(--white)}
.abs{position:absolute}
.serif{font-family:"Old Standard TT",serif;color:var(--ink);font-weight:400}
.btn{position:absolute;display:flex;align-items:center;justify-content:center;gap:14px;font-family:"Poppins",sans-serif;font-weight:700;font-size:11px;color:var(--white);background:var(--green);text-transform:uppercase;letter-spacing:.2px}
.btn-outline{background:transparent;color:var(--ink);border:2px solid var(--green)}
.blob{position:absolute;border-radius:50%}
.art{position:absolute;border-radius:24px}

.hero{position:absolute;left:0;top:0;width:1200px;height:465px;background:var(--hero-bg)}
.brand{position:absolute;display:flex;align-items:center;gap:8px;font-family:"Montserrat",sans-serif;font-weight:500;white-space:nowrap}
.brand-dot{border-radius:50%;background:var(--green);flex:none}
.nav{position:absolute;top:27px;font-size:11px;color:#555;letter-spacing:.2px}
.hero-title{position:absolute;left:189px;top:150px;width:500px;text-align:center;font-size:23px;line-height:35px}
.hero-text{position:absolute;left:189px;top:228px;width:500px;text-align:center;font-size:12px;color:#333}

.h2{position:absolute;font-size:21px;white-space:nowrap}
.lede{position:absolute;font-size:11.5px;font-style:italic;line-height:17px;color:var(--muted)}
.para{position:absolute;font-size:11.5px;line-height:17px;color:#333}

.services-kicker{position:absolute;left:0;width:1200px;top:1205px;text-align:center;font-size:19px}
.services-title{position:absolute;left:0;width:1200px;top:1228px;text-align:center;font-family:"Poppins",sans-serif;font-weight:800;font-size:36px;color:var(--forest)}
.svc-num{position:absolute;font-family:"Old Standard TT",serif;font-size:21px;color:var(--green)}
.svc-title{position:absolute;font-family:"Old Standard TT",serif;font-size:21px;color:var(--ink);white-space:nowrap}
.svc-text{position:absolute;width:240px;font-size:11.5px;line-height:17px;color:#444}

.success{position:absolute;left:0;top:1586px;width:1200px;height:253px;background:linear-gradient(90deg,#3a3327 0%,#0f3a22 35%,#155c2e 60%,#1b3a22 85%,#2c3127 100%)}
.stat-num{position:absolute;font-family:"Poppins",sans-serif;font-weight:700;font-size:16px;color:var(--green)}
.stat-label{position:absolute;font-size:14px;color:#d8d8d8}

.field{position:absolute;height:28px;border:1px solid #2e6e45;background:transparent;font-size:9px;color:#999;padding:0 12px;display:flex;align-items:center}

.footer{position:absolute;left:0;top:2731px;width:1200px;height:317px;background:var(--forest);color:var(--white)}
.f-head{position:absolute;font-family:"Poppins",sans-serif;font-weight:700;font-size:11px;top:45px}
.f-list{position:absolute;top:78px;font-size:12px;line-height:17px;list-style:none}
.social{position:absolute;top:193px;width:14px;height:14px;border-radius:50%;border:2px solid #cfd8d2}
.copyright{position:absolute;left:0;width:1200px;top:297px;text-align:center;font-size:10px;color:#cfd8d2}
</style>
</head>
<body>
<main class="page">

  <div class="blob" style="left:166px;top:586px;width:792px;height:792px;background:var(--blush)"></div>
  <div class="blob" style="left:65px;top:544px;width:142px;height:142px;background:var(--blush)"></div>
  <div class="blob" style="left:990px;top:470px;width:420px;height:720px;background:var(--lavender);border-radius:50% 0 0 50%"></div>
  <div class="blob" style="left:935px;top:1065px;width:166px;height:166px;background:var(--lavender)"></div>
  <div class="blob" style="left:1116px;top:1157px;width:76px;height:76px;background:var(--lavender)"></div>
  <div class="blob" style="left:560px;top:1400px;width:720px;height:720px;background:var(--cream)"></div>
  <div class="blob" style="left:-520px;top:1840px;width:1270px;height:1100px;background:var(--sky)"></div>
  <div class="blob" style="left:1085px;top:2345px;width:82px;height:82px;background:var(--blush)"></div>
  <div class="blob" style="left:1070px;top:2050px;width:84px;height:84px;background:var(--cream)"></div>

  <header class="hero">
    <div class="brand" style="left:174px;top:19px;font-size:15px;color:var(--ink)">
      <span class="brand-dot" style="width:30px;height:30px"></span><span>Bramblet Ecommerce</span>
    </div>
    <span class="nav" style="left:451px">THE TEAM</span>
    <span class="nav" style="left:533px">SOLUTIONS</span>
    <span class="nav" style="left:621px">THE PROCESS</span>
    <span class="nav" style="left:721px">CASE STUDIES</span>
    <span class="nav" style="left:822px">TESTIMONIALS</span>
    <div class="btn" style="left:928px;top:19px;width:97px;height:28px;font-family:'Montserrat',sans-serif;font-weight:500">LET'S TALK</div>

    <h1 class="hero-title serif">Our Company Specializes in Tarvex and Brenvik Management and Growth</h1>
    <p class="hero-text">Lorem ipsum dolor sit amet, consectetur adipiscing elit donec consectetur.</p>
    <div class="btn" style="left:222px;top:276px;width:204px;height:28px">LET'S TALK</div>
    <div class="btn btn-outline" style="left:452px;top:276px;width:204px;height:28px">LEARN MORE</div>
    <div class="art" role="img" aria-label="Illustration of two business people standing beside a potted plant" style="left:690px;top:50px;width:385px;height:355px;background:linear-gradient(160deg,#cdeefa 0%,#e7e6f3 60%,#ececec 100%)"></div>
  </header>

  <h2 class="h2 serif" style="left:174px;top:512px">Out-Perform the Competition with Proprietary Tech.</h2>
  <p class="lede" style="left:174px;top:560px;width:440px">Lorem ipsum dolor sit amet, consectetur adipiscing elit donec consectetur semper nunc in molestie.</p>
  <p class="para" style="left:174px;top:611px;width:440px">Sed velit lectus, porttitor eu convallis sit amet, semper eget mauris. Integer in pulvinar mauris. Donec facilisis placerat</p>
  <div class="btn" style="left:174px;top:682px;width:204px;height:28px">LET'S TALK <span>&rarr;</span></div>
  <div class="art" role="img" aria-label="Illustration of a shopper riding a cart beside a phone showing a product list" style="left:675px;top:509px;width:355px;height:225px;background:linear-gradient(150deg,#e9e9fb 0%,#f6e4ec 70%,#fbeef0 100%)"></div>

  <div class="art" role="img" aria-label="Illustration of a person with a megaphone among browser windows and charts" style="left:160px;top:858px;width:373px;height:249px;background:linear-gradient(150deg,#e7e9f5 0%,#f0dff4 60%,#fbeef0 100%)"></div>
  <h2 class="h2 serif" style="left:551px;top:893px">Active your brand's potential. And your audience's.</h2>
  <p class="lede" style="left:551px;top:945px;width:440px">Lorem ipsum dolor sit amet, consectetur adipiscing elit donec consectetur semper nunc in molestie.</p>
  <p class="para" style="left:551px;top:996px;width:440px">Sed velit lectus, porttitor eu convallis sit amet, semper eget mauris. Integer in pulvinar mauris. Donec facilisis placerat</p>
  <div class="btn" style="left:550px;top:1058px;width:205px;height:28px">SEE OUR RESULTS</div>

  <p class="services-kicker serif">Our Services</p>
  <h2 class="services-title">What we do best</h2>

  <span class="svc-num" style="left:176px;top:1306px">01</span>
  <span class="svc-title" style="left:217px;top:1306px">STRATEGY</span>
  <p class="svc-text" style="left:217px;top:1343px">Sed velit lectus, porttitor eu convallis sit amet, semper eget mauris. Integer in pulvinar mauris. Donec facilisis placerat</p>
  <span class="svc-num" style="left:464px;top:1306px">02</span>
  <span class="svc-title" style="left:505px;top:1306px">TARVEX SERVICES</span>
  <p class="svc-text" style="left:505px;top:1343px">Sed velit lectus, porttitor eu convallis sit amet, semper eget mauris. Integer in pulvinar mauris. Donec facilisis placerat</p>
  <span class="svc-num" style="left:751px;top:1306px">03</span>
  <span class="svc-title" style="left:792px;top:1306px">CONTENT &amp; SOCIAL</span>
  <p class="svc-text" style="left:792px;top:1343px">Sed velit lectus, porttitor eu convallis sit amet, semper eget mauris. Integer in pulvinar mauris. Donec facilisis placerat</p>

  <span class="svc-num" style="left:176px;top:1446px">04</span>
  <span class="svc-title" style="left:217px;top:1446px">WEB DESIGN</span>
  <p class="svc-text" style="left:217px;top:1483px">Sed velit lectus, porttitor eu convallis sit amet, semper eget mauris. Integer in pulvinar mauris. Donec facilisis placerat</p>
  <span class="svc-num" style="left:464px;top:1446px">05</span>
  <span class="svc-title" style="left:505px;top:1446px">STRATEGY</span>
  <p class="svc-text" style="left:505px;top:1483px">Sed velit lectus, porttitor eu convallis sit amet, semper eget mauris. Integer in pulvinar mauris. Donec facilisis placerat</p>
  <span class="svc-num" style="left:751px;top:1446px">06</span>
  <span class="svc-title" style="left:792px;top:1446px">MEDIA BUYING</span>
  <p class="svc-text" style="left:792px;top:1483px">Sed velit lectus, porttitor eu convallis sit amet, semper eget mauris. Integer in pulvinar mauris. Donec facilisis placerat</p>

  <section class="success" role="img" aria-label="Band with a dark green geometric circle and leaf pattern">
    <h2 class="serif abs" style="left:296px;top:42px;font-size:31px;color:var(--white)">Our Success</h2>
    <span class="stat-num" style="left:296px;top:106px">700+</span>
    <span class="stat-label" style="left:296px;top:133px">EMPOYEES</span>
    <span class="stat-num" style="left:508px;top:106px">$2B</span>
    <span class="stat-label" style="left:508px;top:133px">MEDIA MANAGED</span>
    <span class="stat-num" style="left:769px;top:106px">#1</span>
    <span class="stat-label" style="left:769px;top:133px">AWARD-WINNING CULTURE</span>
    <div class="btn" style="left:296px;top:182px;width:204px;height:28px">OUR VISION <span>&rarr;</span></div>
  </section>

  <div class="art" role="img" aria-label="Illustration of a woman with a laptop on a beanbag beside a potted plant" style="left:195px;top:1893px;width:349px;height:267px;background:linear-gradient(150deg,#e6e6f6 0%,#dcdcf6 55%,#f7efd4 100%)"></div>
  <h2 class="h2 serif" style="left:605px;top:1923px">The leading Tarvex agency.</h2>
  <p class="lede" style="left:605px;top:1952px;width:440px">Lorem ipsum dolor sit amet, consectetur adipiscing elit donec consectetur semper nunc in molestie.</p>
  <p class="para" style="left:605px;top:2003px;width:440px">Sed velit lectus, porttitor eu convallis sit amet, semper eget mauris. Integer in pulvinar mauris. Donec facilisis placerat</p>
  <div class="btn" style="left:605px;top:2066px;width:221px;height:29px">LEARN MORE ABOUT TARVEX <span>&rarr;</span></div>

  <h2 class="serif abs" style="left:175px;width:438px;top:2325px;text-align:center;font-size:21px">Stay In the Know</h2>
  <div class="field" style="left:175px;top:2393px;width:210px">Full name *</div>
  <div class="field" style="left:404px;top:2393px;width:209px">Work email *</div>
  <div class="field" style="left:175px;top:2438px;width:438px">What are you interested in ?</div>
  <div class="btn" style="left:175px;top:2483px;width:210px;height:28px">SUBSCRIBE</div>
  <p class="abs" style="left:175px;top:2529px;font-size:9px;color:#666">*By submitting your Email Address, you are agreeing to all conditions of our <u style="color:var(--green-dark)">Privacy Policy</u></p>
  <div class="art" role="img" aria-label="Illustration of a person tapping a large floating screen" style="left:686px;top:2278px;width:379px;height:284px;background:linear-gradient(150deg,#efe4f6 0%,#e6e4fa 50%,#fbe6ea 100%)"></div>

  <footer class="footer">
    <div class="brand" style="left:174px;top:48px;font-size:18px;color:var(--green)">
      <span class="brand-dot" style="width:42px;height:42px"></span><span>Bramblet Ecommerce</span>
    </div>
    <span class="f-head" style="left:462px">About</span>
    <ul class="f-list" style="left:462px"><li>Our Services</li><li>Our Vision</li><li>Results</li></ul>
    <span class="f-head" style="left:569px">Team</span>
    <ul class="f-list" style="left:569px"><li>Culture</li><li>Team</li><li>Careers</li></ul>
    <span class="f-head" style="left:677px">Learn</span>
    <ul class="f-list" style="left:677px;width:80px"><li>Blog</li><li>Guides &amp;</li><li>Webinars</li><li>Events</li><li>News</li><li>Shelf Notes</li><li>Podcast</li><li>The Future</li><li>of the Web</li></ul>
    <span class="f-head" style="left:811px">Contact Us</span>
    <p class="abs" style="left:811px;top:77px;font-size:12px;line-height:18px">555-010-4477<br>hello@BrambletEcommerce.com</p>
    <div class="btn" style="left:811px;top:132px;width:208px;height:28px">CONTACT US</div>
    <span class="social" style="left:811px"></span>
    <span class="social" style="left:839px"></span>
    <span class="social" style="left:867px"></span>
    <p class="copyright">Copyright &copy; 2021 BrambletEcommerce.com. All Rights Reserved. &nbsp;|&nbsp; Privacy Policy</p>
  </footer>

</main>
</body>
</html>
```